Twin Harbor Keystone Method

We are a wealth advisory firm. We need a design that shows our business is built on seven pillars. These seven pillars support all 85 things. These seven pillars form the foundation of our process. As their lives unfold and their needs evolve, they can’t outgrow our process; they’ll grow into it as critical life events occur and their lives progress.

We have an example of pillars, a figure of 8, and trees—we would like it to be modern, clean, and nature-inspired. If you use pillars, they cannot look 80s or like a law office. I am also attaching a picture of our logo and the landing page of our website for reference to our feel and style.
We want to use the language on the sheet with figure 8 in the final design.

Target Market(s)

families and small business owners with 1 million + of investable assets

Industry/Entity Type

Finance

Font styles to use
Sans Serif

Colors
0054AA
0677BA
7BADD7
CADEEF
E8F1F8
FFC000
F8CF3A
FAE287
FDF2CF
FEFAEE
EE7325
F08F49
F5BC92
FAE3D3
FDF4ED

```html
<!DOCTYPE html>
<html lang="en">
<head>
<meta charset="utf-8">
<title>Twin Harbor Keystone Method — 85 Things</title>
<link rel="stylesheet" href="https://fonts.googleapis.com/css2?family=Bebas+Neue&family=Oswald:wght@500&display=swap">
<style>
  :root {
    --blue-deep: #0054AA;
    --blue: #0677BA;
    --blue-soft: #7BADD7;
    --blue-pale: #CADEEF;
    --blue-mist: #E8F1F8;
    --gold: #FFC000;
    --gold-warm: #F8CF3A;
    --gold-soft: #FAE287;
    --gold-pale: #FDF2CF;
    --cream: #FEFAEE;
    --orange: #EE7325;
    --orange-warm: #F08F49;
    --orange-soft: #F5BC92;
    --orange-pale: #FAE3D3;
    --white: #ffffff;
  }
  * { margin: 0; padding: 0; box-sizing: border-box; }
  html, body { width: 863px; height: 1200px; overflow: hidden; background: var(--white); }
  .sheet { position: relative; width: 863px; height: 1200px; background: linear-gradient(180deg, var(--white) 0%, var(--cream) 100%); overflow: hidden; font-family: "Bebas Neue", "Oswald", sans-serif; }

  .side-band { position: absolute; left: 0; top: 0; width: 135px; height: 1200px;
    background: linear-gradient(90deg, var(--blue) 0 74px, var(--blue-deep) 74px 135px); }
  .side-band svg { position: absolute; left: 0; top: 0; }

  .world-map { position: absolute; left: 135px; top: 477px; width: 728px; height: 665px;
    background: radial-gradient(ellipse at 50% 45%, var(--blue-mist) 0%, rgba(232,241,248,0.5) 55%, rgba(255,255,255,0) 80%); }

  .landscape { position: absolute; left: 135px; bottom: 0; }

  .brand { position: absolute; left: 160px; top: 92px; display: flex; align-items: center; gap: 10px; }
  .brand-dot { width: 26px; height: 26px; border-radius: 50%; background: var(--gold); }
  .brand-name { font-family: "Oswald", sans-serif; font-weight: 500; font-size: 20px; letter-spacing: 2px; color: var(--blue-deep); }

  .headline-number { position: absolute; left: 384px; top: 66px; width: 216px; text-align: center;
    font-size: 200px; line-height: 1; letter-spacing: 0;
    background: linear-gradient(135deg, var(--blue) 0%, var(--blue-deep) 100%);
    -webkit-background-clip: text; background-clip: text; color: transparent; }
  .headline-tag { position: absolute; left: 424px; top: 233px; width: 139px; height: 63px; background: var(--blue-deep);
    color: var(--white); font-size: 56px; line-height: 66px; text-align: center; }

  .pill { position: absolute; height: 81px; border-radius: 41px; display: flex; align-items: center; }
  .pill-left { left: 160px; width: 260px; justify-content: flex-end; padding-right: 76px;
    background: linear-gradient(90deg, var(--blue-mist) 0%, rgba(232,241,248,0.7) 70%, rgba(232,241,248,0) 100%); }
  .pill-right { left: 560px; width: 262px; padding-left: 80px;
    background: linear-gradient(270deg, var(--blue-mist) 0%, rgba(232,241,248,0.7) 70%, rgba(232,241,248,0) 100%); }
  .pill-label { color: var(--blue-deep); font-size: 26px; line-height: 24px; letter-spacing: 0.3px; }
  .pill-left .pill-label { text-align: right; }
  .pill-arrow { position: absolute; top: 50%; width: 0; height: 0; transform: translateY(-50%);
    border-top: 14px solid transparent; border-bottom: 14px solid transparent; }
  .pill-left .pill-arrow { right: 42px; border-right: 26px solid var(--blue); }
  .pill-right .pill-arrow { left: 40px; border-left: 26px solid var(--blue); }

  .pillar-stack { position: absolute; left: 0; top: 0; }
  .block-letter { font-family: "Oswald", sans-serif; font-weight: 500; font-size: 17px; fill: var(--white); }
</style>
</head>
<body>
<main class="sheet">

  <aside class="side-band">
    <svg width="135" height="1200" viewBox="0 0 135 1200">
      <text transform="translate(116 1125) rotate(-90)" textLength="1050" lengthAdjust="spacingAndGlyphs"
            font-family="Bebas Neue, Oswald, sans-serif" font-size="104">
        <tspan fill="#FFC000">TWIN HARBOR </tspan><tspan fill="#ffffff">KEYSTONE METHOD</tspan>
      </text>
    </svg>
  </aside>

  <div class="world-map" role="img" aria-label="Faint world map in the background"></div>

  <svg class="landscape" width="728" height="170" viewBox="0 0 728 170" aria-hidden="true">
    <path d="M0 90 C140 40 260 70 380 95 C500 120 620 60 728 70 V170 H0Z" fill="#E8F1F8"/>
    <path d="M0 130 C160 95 300 120 430 135 C560 150 650 115 728 118 V170 H0Z" fill="#CADEEF"/>
  </svg>

  <div class="brand">
    <span class="brand-dot"></span>
    <span class="brand-name">NORTHVALE CAPITAL</span>
  </div>

  <div class="headline-number">85</div>
  <div class="headline-tag">THINGS</div>

  <div class="pill pill-left" style="top:328px"><span class="pill-label">WEALTH<br>MANAGEMENT</span><span class="pill-arrow" style="border-right-color:#F8CF3A"></span></div>
  <div class="pill pill-right" style="top:468px"><span class="pill-arrow" style="border-left-color:#FFC000"></span><span class="pill-label">RISK<br>MANAGEMENT</span></div>
  <div class="pill pill-left" style="top:549px"><span class="pill-label">TAX</span><span class="pill-arrow" style="border-right-color:#F08F49"></span></div>
  <div class="pill pill-right" style="top:688px"><span class="pill-arrow" style="border-left-color:#EE7325"></span><span class="pill-label">ESTATE</span></div>
  <div class="pill pill-left" style="top:776px"><span class="pill-label">CASH</span><span class="pill-arrow" style="border-right-color:#7BADD7"></span></div>
  <div class="pill pill-right" style="top:919px"><span class="pill-arrow" style="border-left-color:#0677BA"></span><span class="pill-label">PHILANTHROPY</span></div>
  <div class="pill pill-left" style="top:1004px"><span class="pill-label">VALUE ADDED<br>SERVICES</span><span class="pill-arrow" style="border-right-color:#0054AA"></span></div>

  <svg class="pillar-stack" width="863" height="1200" viewBox="0 0 863 1200">
    <!-- G -->
    <g transform="translate(0 1000)">
      <polygon points="402,0 504,-17 578,24 474,46" fill="#0677BA"/>
      <polygon points="402,0 474,46 474,122 402,81" fill="#003f82"/>
      <polygon points="474,46 578,24 578,110 474,122" fill="#0054AA"/>
      <g transform="translate(436 48)" fill="none" stroke="#fff" stroke-width="2.5">
        <polygon points="-8,-12 8,-12 12,-6 0,8 -12,-6"/><path d="M-16 12 q10 -6 18 0 l10 -4"/>
      </g>
      <text class="block-letter" x="495" y="96">G</text>
    </g>
    <!-- F -->
    <g transform="translate(0 888)">
      <polygon points="402,0 504,-17 578,24 474,46" fill="#3f93c9"/>
      <polygon points="402,0 474,46 474,122 402,81" fill="#05609a"/>
      <polygon points="474,46 578,24 578,110 474,122" fill="#0677BA"/>
      <path transform="translate(436 42)" d="M0 6 C-14 -4 -8 -16 0 -8 C8 -16 14 -4 0 6Z M-14 2 v16 M14 2 v16" fill="#fff" stroke="#fff" stroke-width="3"/>
      <text class="block-letter" x="495" y="96">F</text>
    </g>
    <!-- E -->
    <g transform="translate(0 776)">
      <polygon points="402,0 504,-17 578,24 474,46" fill="#CADEEF"/>
      <polygon points="402,0 474,46 474,122 402,81" fill="#5f98c9"/>
      <polygon points="474,46 578,24 578,110 474,122" fill="#7BADD7"/>
      <g transform="translate(436 44) rotate(25)" fill="none" stroke="#fff" stroke-width="2.5">
        <rect x="-16" y="-10" width="32" height="20" rx="2"/><circle r="6"/>
      </g>
      <text class="block-letter" x="495" y="96">E</text>
    </g>
    <!-- D -->
    <g transform="translate(0 664)">
      <polygon points="402,0 504,-17 578,24 474,46" fill="#F5BC92"/>
      <polygon points="402,0 474,46 474,122 402,81" fill="#d5601a"/>
      <polygon points="474,46 578,24 578,110 474,122" fill="#EE7325"/>
      <g transform="translate(436 42)" fill="none" stroke="#fff" stroke-width="2.5">
        <path d="M-12 -2 L0 -14 L12 -2 M-8 -4 v12 h16 v-12"/><path d="M-14 14 q10 6 26 -2"/>
      </g>
      <text class="block-letter" x="495" y="96">D</text>
    </g>
    <!-- C -->
    <g transform="translate(0 552)">
      <polygon points="402,0 504,-17 578,24 474,46" fill="#FAE3D3"/>
      <polygon points="402,0 474,46 474,122 402,81" fill="#e07a36"/>
      <polygon points="474,46 578,24 578,110 474,122" fill="#F08F49"/>
      <g transform="translate(436 44)" fill="none" stroke="#fff" stroke-width="2.5">
        <path d="M-10 -16 h14 l8 8 v24 h-22z"/><circle cx="-6" cy="4" r="7"/><path d="M4 -2 h6 M4 6 h6"/>
      </g>
      <text class="block-letter" x="495" y="96">C</text>
    </g>
    <!-- B -->
    <g transform="translate(0 440)">
      <polygon points="402,0 504,-17 578,24 474,46" fill="#FDF2CF"/>
      <polygon points="402,0 474,46 474,122 402,81" fill="#e6a800"/>
      <polygon points="474,46 578,24 578,110 474,122" fill="#FFC000"/>
      <g transform="translate(436 44)" fill="none" stroke="#fff" stroke-width="3">
        <circle r="14" stroke-dasharray="6 3"/><path d="M0 -7 v8 M0 5 v2"/>
      </g>
      <text class="block-letter" x="495" y="96">B</text>
    </g>
    <!-- A -->
    <g transform="translate(0 328)">
      <polygon points="402,0 504,-17 578,24 474,46" fill="#FEFAEE"/>
      <polygon points="402,0 474,46 474,122 402,81" fill="#F8CF3A"/>
      <polygon points="474,46 578,24 578,110 474,122" fill="#FAE287"/>
      <g transform="translate(436 46)" fill="none" stroke="#fff" stroke-width="3">
        <path d="M-6 -14 h12 l-3 6 q12 8 6 20 h-18 q-6 -12 6 -20z"/><path d="M8 10 h10 M8 16 h10"/>
      </g>
      <text class="block-letter" x="495" y="96" style="fill:#0054AA">A</text>
    </g>
  </svg>

</main>
</body>
</html>
```